Agriculture Business Card

I want to use my existing logo and use my tagline of "Don't Guess...Soil Test" on the card. Looking for a double sided card that will really get peoples attention.
Contact Info:
Marlow Field Crop Partners
Calvin Brusk
2716 K Lane
Larkmoor, KS 66591
402-555-0143
calvin.r.brusk@fieldmailbox.net

```html
<!DOCTYPE html>
<html lang="en">
<head>
<meta charset="utf-8">
<title>Marlow Field Crop Partners – Business Card</title>
<link rel="stylesheet" href="https://fonts.googleapis.com/css2?family=Montserrat:wght@400;500&family=Yanone+Kaffeesatz:wght@600&display=swap">
<style>
  :root{
    --backdrop:#2b2b2d;
    --card-white:#ffffff;
    --soil:#a26a50;
    --soil-dark:#95583f;
    --leaf:#3aab48;
    --leaf-light:#6dbd45;
    --gold:#f7b21c;
    --ink:#555558;
  }
  *{box-sizing:border-box;margin:0;padding:0}
  html,body{width:1200px;height:839px;overflow:hidden;background:var(--backdrop)}
  .stage{position:relative;width:1200px;height:839px;display:flex;justify-content:center;align-items:center;gap:70px}
  .card{width:360px;height:630px;border-radius:26px;position:relative;overflow:hidden;box-shadow:0 18px 40px rgba(0,0,0,.45);display:flex;flex-direction:column;align-items:center;text-align:center}
  .card--front{background:var(--card-white)}
  .card--back{background:var(--soil)}

  .brand{margin-top:110px;display:flex;flex-direction:column;align-items:center;gap:14px}
  .brand__dot{width:44px;height:44px;border-radius:50%;background:var(--gold)}
  .brand__name{font-family:"Yanone Kaffeesatz",sans-serif;font-weight:600;font-size:40px;line-height:1;color:var(--soil-dark);max-width:260px;text-align:center}

  .person{margin-top:52px;font-family:"Montserrat",sans-serif;font-weight:500;font-size:27px;letter-spacing:1px;color:var(--soil-dark);text-transform:uppercase}

  .contact-icons{margin-top:44px;display:flex;align-items:center;gap:8px}
  .rule{display:block;height:1.5px;background:var(--leaf-light)}
  .rule--green{width:60px}
  .rule--gold{width:110px;background:var(--gold);margin:18px auto}
  .icon{width:30px;height:30px;border-radius:6px;background:var(--leaf);display:flex;align-items:center;justify-content:center}
  .icon svg{width:18px;height:18px}

  .contact{margin-top:22px;font-family:"Montserrat",sans-serif;font-size:15px;line-height:1.55;color:var(--ink)}
  .address{font-family:"Montserrat",sans-serif;font-size:15.5px;line-height:1.55;color:var(--ink)}

  .back__brand{margin-top:220px;display:flex;flex-direction:column;align-items:center;gap:14px}
  .back__brand .brand__dot{background:var(--leaf-light)}
  .back__brand .brand__name{color:var(--gold)}
  .tagline{position:absolute;bottom:70px;left:0;right:0;text-align:center;font-family:"Montserrat",sans-serif;font-size:19px;color:var(--gold);letter-spacing:.3px}
</style>
</head>
<body>
<main class="stage">
  <section class="card card--front" aria-label="Card front">
    <div class="brand">
      <span class="brand__dot"></span>
      <h1 class="brand__name">Marlow Field Crop Partners</h1>
    </div>
    <h2 class="person">Calvin Brusk</h2>
    <div class="contact-icons">
      <span class="rule rule--green"></span>
      <span class="icon" aria-label="Phone">
        <svg viewBox="0 0 24 24" fill="#fff"><path d="M6.6 10.8a15.1 15.1 0 0 0 6.6 6.6l2.2-2.2c.3-.3.7-.4 1-.2 1.1.4 2.3.6 3.6.6.6 0 1 .4 1 1V20c0 .6-.4 1-1 1A17 17 0 0 1 3 4c0-.6.4-1 1-1h3.5c.6 0 1 .4 1 1 0 1.3.2 2.5.6 3.6.1.3 0 .7-.2 1z"/></svg>
      </span>
      <span class="icon" aria-label="Email">
        <svg viewBox="0 0 24 24" fill="#fff"><path d="M3 6h18v12H3z"/><path d="M3 6l9 7 9-7" fill="none" stroke="#3aab48" stroke-width="1.8"/></svg>
      </span>
      <span class="icon" aria-label="Web">
        <svg viewBox="0 0 24 24" fill="none" stroke="#fff" stroke-width="2"><circle cx="12" cy="12" r="8.5"/><path d="M3.5 12h17M12 3.5c3 3 3 14 0 17M12 3.5c-3 3-3 14 0 17"/></svg>
      </span>
      <span class="rule rule--green"></span>
    </div>
    <p class="contact">402-555-0143<br>calvin.r.brusk@fieldmailbox.net</p>
    <span class="rule rule--gold"></span>
    <p class="address">2716 K Lane<br>Larkmoor, KS 66591</p>
  </section>

  <section class="card card--back" aria-label="Card back">
    <div class="back__brand">
      <span class="brand__dot"></span>
      <p class="brand__name">Marlow Field Crop Partners</p>
    </div>
    <p class="tagline">Don't Guess...Soil Test</p>
  </section>
</main>
</body>
</html>
```